Layout für Broschüre für chemiefreie Lösung, Kühlwasser aufzubereiten
Zielgruppe
VELTROMAX hat eine Technologie entwickelt, die in der Industrie eingesetzt wird um in geschlossenen und offenen Kühlkreisläufen ohne Biozide und Korrosion Inhibitoren das Kühlwasser aufzubereiten. Mit VELTROMAX haben die Unternehmen eine chemiefreie Lösungen gegen Biofouling, Korrosion und Kalk. Zielgruppe sind alle Unternehmen die etwas produzieren oder Klimaanlagen / Heizungssysteme betreiben. Es geht um zukunftsorientierte und vor allem nachhaltige Technologie ohne Einsatz von Chemie.
Aufgabenstellung
Wir suchen für die Broschüre ein neues Layout, dass geradlinig und klar strukturiert ist, vor allem modern. Die Broschüre sollte DIN A 4 - Format sein in der gewohnten Struktur Umschlagseite innen und außen und 8 - 10 Innenseiten. Im Layout sollte ein roter Faden zu erkennen sein, aber nicht jede Seite gleich aussehen. Die Anlagen sind nur beispielhaft vom bestehenden Material und sollten vom Layout keinesfalls eine Orientierung geben, denn das soll verändert werden. Die Anlagen sind für einen inhaltlichen Überblick.

```html
<!DOCTYPE html>
<html lang="de">
<head>
<meta charset="UTF-8">
<title>Chemiefrei – Wirkungsweise</title>
<link rel="stylesheet" href="https://fonts.googleapis.com/css2?family=Arimo:wght@400;700&family=Lato:wght@400;700&family=Montserrat:wght@400;500&display=swap">
<style>
  :root {
    --backdrop: #e4e4e2;
    --paper: #fbfbf9;
    --green: #4cbb3c;
    --band: #c9c8c5;
    --ink: #1d1d1b;
    --ink-soft: #55554f;
    --title-grey: #b4b4b0;
    --circle-1: #8d8d8b;
    --circle-2: #9a9a98;
    --circle-3: #b0b0ae;
    --rule: #9a9a96;
  }
  * { box-sizing: border-box; margin: 0; padding: 0; }
  html, body { width: 1200px; height: 900px; overflow: hidden; }
  body { background: var(--backdrop); font-family: "Lato", sans-serif; color: var(--ink); position: relative; }

  .page { position: absolute; top: 40px; width: 580px; height: 820px; background: var(--paper); }
  .page--left { left: 20px; }
  .page--right { left: 600px; border-left: 1px solid #e2e2df; }

  .section-title {
    position: absolute; left: 113px; top: 136px; width: 357px; height: 69px;
    border: 3px solid var(--green);
    display: flex; align-items: center; justify-content: center;
    font-family: "Montserrat", sans-serif; font-weight: 500; font-size: 24px;
    letter-spacing: 3px; color: var(--title-grey);
  }
  .intro {
    position: absolute; left: 40px; right: 40px; top: 295px;
    text-align: center; text-transform: uppercase;
    font-size: 14px; line-height: 24px; letter-spacing: 1.2px; color: var(--ink);
  }
  .steps-band {
    position: absolute; left: 0; right: 0; top: 361px; height: 352px;
    background: var(--band);
    display: grid; grid-template-columns: repeat(3, 1fr); padding: 0 22px;
  }
  .step { display: flex; flex-direction: column; align-items: center; text-align: center; padding: 57px 8px 0; }
  .step__dot { width: 98px; height: 108px; border-radius: 50%; margin-bottom: 36px; }
  .step:nth-child(1) .step__dot { background: var(--circle-1); }
  .step:nth-child(2) .step__dot { background: var(--circle-2); }
  .step:nth-child(3) .step__dot { background: var(--circle-3); }
  .step__label { font-weight: 700; font-size: 14px; letter-spacing: 1px; color: var(--green); }
  .step__lead { margin-top: 6px; font-size: 11px; letter-spacing: 1px; text-transform: uppercase; color: var(--ink-soft); }
  .step__text { margin-top: 18px; font-size: 10px; line-height: 14px; color: var(--ink-soft); max-width: 150px; }

  .folio { position: absolute; left: 40px; right: 40px; top: 793px; border-top: 1px solid var(--rule); padding-top: 5px; font-size: 9px; color: var(--ink-soft); }
  .page--right .folio { text-align: right; }

  .heading {
    position: absolute; left: 78px; top: 68px; width: 311px;
    font-family: "Montserrat", sans-serif; font-weight: 500; font-size: 24px;
    letter-spacing: 3px; color: var(--title-grey);
    padding-bottom: 4px; border-bottom: 4px solid var(--green);
  }
  .body-copy {
    position: absolute; left: 78px; top: 136px; width: 424px;
    font-family: "Arimo", sans-serif; font-size: 13px; line-height: 17px; color: var(--ink);
  }
  .feature-image {
    position: absolute; left: 81px; top: 271px; width: 412px; height: 377px;
    border: 4px solid var(--green);
    background:
      radial-gradient(ellipse 60% 28% at 55% 22%, rgba(90,190,235,0.75), transparent 70%),
      radial-gradient(ellipse 12% 10% at 52% 58%, rgba(80,170,210,0.6), transparent 80%),
      linear-gradient(180deg, #1f4f73 0%, #123048 26%, #0b1216 45%, #0a0c0d 100%);
  }
  .caption {
    position: absolute; left: 180px; top: 631px; width: 214px; height: 44px;
    background: #dcdcd9;
    display: flex; align-items: center; justify-content: center;
    font-family: "Arimo", sans-serif; font-weight: 700; font-size: 12px;
    letter-spacing: 2px; color: var(--green);
  }
</style>
</head>
<body>
  <section class="page page--left">
    <h2 class="section-title">WIRKUNGSWEISE</h2>
    <p class="intro">Gent pediscitate peliquo destiam, quissus aut atur? Qui<br>aut officil maximaion eum ullupta turi</p>
    <div class="steps-band">
      <div class="step">
        <div class="step__dot"></div>
        <div class="step__label">SCHRITT 1</div>
        <div class="step__lead">Inis enturit dolupta</div>
        <p class="step__text">Calzium(+) und Bicarbonat(-) liegen gebunden im Wasser vor. Weiterhin Salze, Chloride, Sulfate, Metallionen, Mikrobiologie</p>
      </div>
      <div class="step">
        <div class="step__dot"></div>
        <div class="step__label">SCHRITT 2</div>
        <div class="step__lead">Explique coreniendi</div>
        <p class="step__text">Energieeintrag über Frequenz-Impulstechnologie</p>
      </div>
      <div class="step">
        <div class="step__dot"></div>
        <div class="step__label">SCHRITT 3</div>
        <div class="step__lead">Ga. Bit laborest, se-</div>
        <p class="step__text">Alle +/- geladenen Teilchen geraten in Schwingung. (Wassermoleküle als Dipole) Gelöste Ionen reagieren mit</p>
      </div>
    </div>
    <div class="folio">4 Chemiefrei</div>
  </section>

  <section class="page page--right">
    <h2 class="heading">ÜBERSCHRIFT</h2>
    <p class="body-copy">Lorem ipsum dolor sit amet, consetetur sadipscing elitr, sed diam nonumy eirmod tempor invidunt ut labore et dolore magna aliquyam erat, sed diam voluptua. At vero eos et accusam et justo duo dolores et ea rebum. Stet clita kasd gubergren, no sea takimata sanctus est Lorem ipsum dolor sit amet.</p>
    <div class="feature-image" role="img" aria-label="Nahaufnahme eines fallenden Wassertropfens mit blau leuchtender Wasseroberfläche vor dunklem Hintergrund"></div>
    <div class="caption">BILDUNTERSCHRIFT</div>
    <div class="folio">Chemiefrei 5</div>
  </section>
</body>
</html>
```